Improved Business Card, Government Contracting

We are looking to update the design of our business cards. We would like to create a template that can be used for future employees and easy to update.

Halvorsen Advisory Partners, LLC is a Service Disabled Veteran Owned Small Business with headquarters located in Fairhollow, NE. Our current website is www.hapteam.com. We have contracts in KS and VA with expansion opportunities in various other states. Our primary line of work is within government contracting and providing consulting services to various organizations within the Bureau of Frontier Works. We would like to project a professional image of our company that is consistent with the industry. Provided are previous versions of our business card template that shows our logo as well. We would like to make sure the information on the cards are easily noticeable .

Target Market(s)

Government Officials
Fellow Small Business Contractors
Large Business Contractors (ex. TRUX, Keswell Barnaby, Pryde Okonjo Whitcombe)

Industry/Entity Type

Business

Contact Information for Business Card

Dale Fenwick
Office Manager
Halvorsen Advisory Partners
Ph: 402.555.0172
Email: d.fenwick@hapteam.us
www.hapteam.com

Requirements
Must have
• The business mailing address is:
• 31842 204th Lane
• Fairhollow, NE 66099
Nice to have
• Embossed lettering

```html
<!DOCTYPE html>
<html lang="en">
<head>
<meta charset="utf-8">
<title>Halvorsen Advisory Partners – Business Card</title>
<link rel="stylesheet" href="https://fonts.googleapis.com/css2?family=Noto+Sans:wght@400;700&display=swap">
<style>
  :root {
    --brand-blue: #3b57a6;
    --ink-blue: #2c4797;
    --accent-yellow: #f1ea4f;
    --card-white: #ffffff;
    --page-bg: #f2f2f2;
    --card-shadow: rgba(0, 0, 0, 0.16);
  }
  * { box-sizing: border-box; margin: 0; padding: 0; }
  html, body {
    width: 1200px;
    height: 873px;
    overflow: hidden;
  }
  body {
    background: var(--page-bg);
    font-family: "Noto Sans", Verdana, sans-serif;
    display: flex;
    align-items: center;
    justify-content: center;
    gap: 56px;
  }
  .card {
    width: 510px;
    height: 291px;
    border-radius: 3px;
    box-shadow: 0 6px 18px var(--card-shadow);
    overflow: hidden;
    display: flex;
  }
  .company-name {
    color: var(--accent-yellow);
    font-weight: 400;
    text-transform: uppercase;
    text-align: center;
    letter-spacing: 0.06em;
    line-height: 1.25;
  }

  /* Back side: brand panel + contact details */
  .card-back { background: var(--card-white); }
  .card-back .brand-panel {
    width: 44%;
    background: var(--brand-blue);
    display: flex;
    align-items: center;
    justify-content: center;
    padding: 20px;
  }
  .card-back .company-name { font-size: 16px; }
  .contact {
    flex: 1;
    padding: 32px 20px 0 26px;
    color: var(--ink-blue);
  }
  .contact .person-name {
    font-size: 26px;
    font-weight: 700;
    line-height: 1.1;
  }
  .contact .job-title {
    font-size: 11px;
    margin: 3px 0 18px;
  }
  .contact .details {
    list-style: none;
    font-size: 14px;
    line-height: 1.42;
    white-space: nowrap;
  }

  /* Front side: full brand colour */
  .card-front {
    background: var(--brand-blue);
    align-items: center;
    justify-content: center;
  }
  .card-front .company-name { font-size: 26px; max-width: 300px; }
</style>
</head>
<body>
  <section class="card card-back" aria-label="Business card, back">
    <div class="brand-panel">
      <p class="company-name">Halvorsen Advisory Partners</p>
    </div>
    <div class="contact">
      <h1 class="person-name">Dale Fenwick</h1>
      <p class="job-title">Office Manager</p>
      <ul class="details">
        <li>402.555.0172</li>
        <li>d.fenwick@hapteam.us</li>
        <li>Halvorsen Advisory Partners</li>
        <li>31842 204th Lane</li>
        <li>Fairhollow, NE 66099</li>
        <li>www.hapteam.com</li>
      </ul>
    </div>
  </section>

  <section class="card card-front" aria-label="Business card, front">
    <p class="company-name">Halvorsen Advisory Partners</p>
  </section>
</body>
</html>
```